Tarvel Ridge LLC

Need Professional Business cards for New Investment Fund

Target Market(s)

High Quality investors

Industry/Entity Type

Financial

Contact Information for Business Card

Phone Number +1 555 284 6193
Name Pavel Orlinsky
Title Fund Manager
email po@FundTarvel.example
Website www.FundTarvel.example

Colors

Designer to choose colors to be used in the design.

Requirements
Must have
• Must have our Logo and all of the above. Must be made so lettering and loge can be raised

```html
<!DOCTYPE html>
<html lang="en">
<head>
<meta charset="utf-8">
<title>Tarvel Ridge LLC – Business Card</title>
<link rel="stylesheet" href="https://fonts.googleapis.com/css2?family=Montserrat:wght@400;600;700&display=swap">
<style>
  :root {
    --backdrop: #3a2f2a;
    --card: #2b2b2d;
    --card-pattern: #323235;
    --accent: #27e41c;
    --ink: #f2f2f2;
    --ink-soft: #d6d6d6;
  }
  * { box-sizing: border-box; margin: 0; padding: 0; }
  html, body {
    width: 1200px; height: 800px; overflow: hidden;
    background: var(--backdrop);
    font-family: "Montserrat", Arial, sans-serif;
  }
  .canvas {
    position: relative; width: 1200px; height: 800px;
    display: flex; flex-direction: column; align-items: center; justify-content: center; gap: 40px;
  }
  .card {
    position: relative; width: 630px; height: 360px;
    background: var(--card);
    border: 3px solid var(--accent);
    overflow: hidden;
  }
  /* Back side */
  .card-back__pattern {
    position: absolute; inset: 0;
    background: linear-gradient(135deg, var(--card-pattern), var(--card));
  }
  .wordmark {
    position: absolute; display: flex; align-items: center; gap: 8px;
    font-weight: 700; color: var(--ink); text-transform: uppercase; letter-spacing: 1px;
  }
  .wordmark__square { width: 12px; height: 12px; background: var(--accent); }
  .card-back .wordmark { right: 34px; bottom: 40px; font-size: 15px; }

  /* Front side */
  .holder { position: absolute; left: 40px; top: 118px; }
  .holder__name {
    color: var(--accent); font-weight: 700; font-size: 20px;
    text-transform: uppercase; letter-spacing: 0.5px;
  }
  .holder__title { color: var(--ink-soft); font-size: 14px; margin-top: 2px; }
  .rule { position: absolute; height: 1.5px; background: var(--ink-soft); }
  .rule--middle { left: 40px; top: 172px; width: 420px; }
  .rule--bottom { left: 250px; top: 310px; width: 345px; }
  .contacts { position: absolute; left: 40px; top: 188px; list-style: none; }
  .contacts__item {
    display: flex; align-items: center; gap: 10px;
    color: var(--ink); font-size: 14px; line-height: 24px;
  }
  .contacts__icon { width: 13px; height: 13px; flex: none; }
  .card-front .wordmark { left: 470px; top: 158px; font-size: 15px; }
</style>
</head>
<body>
<main class="canvas">
  <section class="card card-back" aria-label="Card back">
    <div class="card-back__pattern" role="img" aria-label="Repeating tone-on-tone brand pattern across the card back"></div>
    <div class="wordmark"><span class="wordmark__square"></span>Tarvel Ridge</div>
  </section>

  <section class="card card-front" aria-label="Card front">
    <div class="holder">
      <h1 class="holder__name">Pavel Orlinsky</h1>
      <p class="holder__title">Fund Manager</p>
    </div>
    <div class="rule rule--middle"></div>
    <ul class="contacts">
      <li class="contacts__item">
        <svg class="contacts__icon" viewBox="0 0 24 24" fill="var(--accent)"><path d="M6.6 10.8a15.1 15.1 0 0 0 6.6 6.6l2.2-2.2a1 1 0 0 1 1-.25 11.4 11.4 0 0 0 3.6.57 1 1 0 0 1 1 1V20a1 1 0 0 1-1 1A17 17 0 0 1 3 4a1 1 0 0 1 1-1h3.5a1 1 0 0 1 1 1c0 1.25.2 2.45.57 3.57a1 1 0 0 1-.25 1z"/></svg>
        +1 555 284 6193
      </li>
      <li class="contacts__item">
        <svg class="contacts__icon" viewBox="0 0 24 24" fill="var(--accent)"><path d="M2 5h20v14H2z"/><path d="M2 5l10 8 10-8" fill="none" stroke="var(--card)" stroke-width="2"/></svg>
        po@FundTarvel.example
      </li>
      <li class="contacts__item">
        <svg class="contacts__icon" viewBox="0 0 24 24" fill="none" stroke="var(--accent)" stroke-width="2.4"><circle cx="12" cy="12" r="9.5"/><path d="M2.5 12h19M12 2.5c3 3 3 16 0 19M12 2.5c-3 3-3 16 0 19"/></svg>
        www.FundTarvel.example
      </li>
    </ul>
    <div class="wordmark"><span class="wordmark__square"></span>Tarvel Ridge</div>
    <div class="rule rule--bottom"></div>
  </section>
</main>
</body>
</html>
```